Business Card Design Project

Im an electrician and my company name is Brightway Electrical
My main work is installing Lighting and Power Points, Home Theater Systems, TVS, Phones and Data
Im looking a business card, something nice, clean, modern and not to cluttered
Im open to sugestions
I dont mind if the "Services" is on the back on the business card
colours black, grey, white or the blue colour of my logo are prefered but not compulsory
any questions just message me
and please make it so if i need to edit the writing can do it easy. maybe by making it a seperate layer ?
My Details are.
Name - Peter Hollis
Job Title - Licenced Electrician
Mobile - 027 530 2174
Email - peter@brightwayelectrical.co.nz
Web - www.brightwayelectrical.co.nz
Services
Residential / Commercial
Lighting & Power
Heating & Ventilation
Automation
Phone & Data
Home Cinema
Sound Systems
TV, Antenna & Satellite
Digital Upgrades

```html
<!DOCTYPE html>
<html lang="en">
<head>
<meta charset="utf-8">
<title>Brightway Electrical – Business Card</title>
<link rel="stylesheet" href="https://fonts.googleapis.com/css2?family=Exo+2:ital,wght@0,400;0,600;0,700;1,400&display=swap">
<style>
  :root {
    --backdrop: #1c1c1d;
    --card-black: #141516;
    --card-black-soft: #1d1e20;
    --accent-blue: #00b3cc;
    --steel-grey: #8e949b;
    --light-grey: #c9ccd0;
    --ink: #0d0d0d;
  }
  * { box-sizing: border-box; margin: 0; padding: 0; }
  html, body { width: 1200px; height: 900px; overflow: hidden; }
  body {
    background: var(--backdrop);
    font-family: "Exo 2", "Helvetica Neue", Arial, sans-serif;
    position: relative;
  }
  .card {
    position: absolute;
    width: 500px;
    height: 286px;
    overflow: hidden;
    box-shadow: 0 14px 30px rgba(0,0,0,.55);
  }

  /* ---------- Back side: services ---------- */
  .card-back {
    left: 60px; top: 307px;
    background: linear-gradient(160deg, var(--card-black-soft), var(--card-black));
  }
  .card-back .grey-band {
    position: absolute; left: 0; top: 0;
    width: 150px; height: 100%;
    background: var(--steel-grey);
  }
  .card-back .brand {
    position: absolute; left: 200px; top: 40px;
    display: flex; align-items: center; gap: 10px;
  }
  .brand-square {
    width: 22px; height: 22px; background: var(--accent-blue);
  }
  .brand-name {
    font-weight: 600; color: var(--accent-blue);
    text-transform: uppercase; letter-spacing: 1.5px; line-height: 1.05;
  }
  .card-back .brand-name { font-size: 22px; }
  .services {
    position: absolute; left: 200px; top: 118px;
    display: grid; grid-template-columns: auto auto; column-gap: 22px; row-gap: 3px;
    list-style: none;
    font-style: italic; font-size: 12.5px; color: var(--light-grey);
  }
  .services li::before { content: "• "; color: var(--steel-grey); }
  .card-back .web {
    position: absolute; left: 200px; bottom: 30px;
    font-size: 15px; font-weight: 600; font-style: italic; color: var(--accent-blue);
  }

  /* ---------- Front side: contact ---------- */
  .card-front {
    left: 640px; top: 307px;
    background: var(--accent-blue);
  }
  .card-front .top-panel {
    position: absolute; left: 0; top: 0; width: 100%; height: 128px;
    background: linear-gradient(160deg, var(--card-black-soft), var(--card-black));
  }
  .card-front .divider-line {
    position: absolute; left: 0; top: 128px; width: 100%; height: 7px;
    background: var(--steel-grey);
  }
  .card-front .brand {
    position: absolute; right: 34px; top: 40px;
    display: flex; align-items: center; gap: 12px;
  }
  .card-front .brand-name { font-size: 30px; }
  .holder {
    position: absolute; left: 30px; top: 166px; width: 180px; text-align: center;
  }
  .holder-name {
    font-weight: 700; font-size: 24px; letter-spacing: .5px; color: var(--ink);
    text-transform: uppercase; line-height: 1;
  }
  .holder-title {
    font-weight: 600; font-size: 10.5px; letter-spacing: .4px; color: var(--ink);
    text-transform: uppercase; margin-top: 3px;
  }
  .contact-rule {
    position: absolute; left: 228px; top: 162px; width: 1px; height: 92px;
    background: rgba(0,0,0,.25);
  }
  .contacts {
    position: absolute; left: 244px; top: 162px; list-style: none;
    font-size: 12.5px; font-weight: 600; color: var(--ink); text-transform: uppercase;
  }
  .contacts li { display: flex; align-items: center; gap: 9px; height: 31px; }
  .contacts svg { width: 13px; height: 13px; flex: none; }
</style>
</head>
<body>

<section class="card card-back" aria-label="Business card, back">
  <div class="grey-band"></div>
  <div class="brand">
    <div class="brand-square"></div>
    <div class="brand-name">Brightway<br>Electrical</div>
  </div>
  <ul class="services">
    <li>Residential / Commercial</li><li>Lighting &amp; Power</li>
    <li>Heating &amp; Ventilation</li><li>Automation</li>
    <li>Phone &amp; Data</li><li>Home Cinema</li>
    <li>TV, Antenna &amp; Satellite</li><li>Sound Systems</li>
    <li>Digital Upgrades</li>
  </ul>
  <div class="web">www.brightwayelectrical.co.nz</div>
</section>

<section class="card card-front" aria-label="Business card, front">
  <div class="top-panel"></div>
  <div class="divider-line"></div>
  <div class="brand">
    <div class="brand-square"></div>
    <div class="brand-name">Brightway Electrical</div>
  </div>
  <div class="holder">
    <div class="holder-name">Peter Hollis</div>
    <div class="holder-title">Licenced Electrician</div>
  </div>
  <div class="contact-rule"></div>
  <ul class="contacts">
    <li>
      <svg viewBox="0 0 16 16" fill="#555b61"><rect x="4" y="1" width="8" height="14" rx="1.5"/><rect x="5.5" y="3" width="5" height="8" fill="#00b3cc"/></svg>
      027 530 2174
    </li>
    <li>
      <svg viewBox="0 0 16 16" fill="none" stroke="#555b61" stroke-width="1.6"><rect x="1.5" y="3.5" width="13" height="9"/><path d="M1.5 3.5 8 9l6.5-5.5"/></svg>
      peter@brightwayelectrical.co.nz
    </li>
    <li>
      <svg viewBox="0 0 16 16" fill="none" stroke="#555b61" stroke-width="1.4"><circle cx="8" cy="8" r="6.5"/><ellipse cx="8" cy="8" rx="2.8" ry="6.5"/><path d="M1.5 8h13"/></svg>
      www.brightwayelectrical.co.nz
    </li>
  </ul>
</section>

</body>
</html>
```